Ridgeline Orchards Organic Cherry POS card 7x11

We are wanting to create a one-sided 7 x 11 organic cherry card that is eye catching and informative.This should be clear and easy to read and not cluttered. We use these cards as a display in grocery stores, demo stands, and other events to market Organic Ridgeline Sweet Orchards. We have a few facts that we would like displayed on the card (see attachment).

Target Market(s)

Consumers

Industry/Entity Type

Agriculture

Requirements
Must have
• Natural color palettes
• Easy to read
• Ridgeline Orchards
Nice to have
• Unique, realistic cherry design

```html
<!DOCTYPE html>
<html lang="en">
<head>
<meta charset="utf-8">
<title>Ridgeline Orchards – Organic Cherry Card</title>
<link rel="stylesheet" href="https://fonts.googleapis.com/css2?family=Montserrat:wght@500;600;700&family=Roboto:wght@300;400;500&display=swap">
<style>
  :root {
    --paper: #ffffff;
    --cherry-deep: #2a0608;
    --cherry-mid: #6e1118;
    --cherry-bright: #9c1c24;
    --stem-green: #4f7a2c;
    --brand-red: #7a1420;
    --band: rgba(52, 8, 10, 0.62);
    --frame: rgba(255, 255, 255, 0.85);
    --ink-light: #ffffff;
  }
  * { margin: 0; padding: 0; box-sizing: border-box; }
  html, body { width: 764px; height: 1200px; overflow: hidden; background: var(--paper); }
  .card { position: relative; width: 764px; height: 1200px; background: var(--paper); }

  .masthead {
    position: absolute; top: 0; left: 0; width: 764px; height: 190px;
    display: flex; align-items: center; justify-content: center; gap: 18px;
  }
  .brand-dot { width: 54px; height: 54px; border-radius: 50%; background: var(--brand-red); }
  .brand-name {
    font-family: "Montserrat", sans-serif; font-weight: 600; font-size: 44px;
    color: var(--brand-red); letter-spacing: 0.5px;
  }

  .cherry-photo {
    position: absolute; top: 190px; left: 0; width: 764px; height: 1010px;
    background:
      radial-gradient(ellipse 210px 190px at 330px 150px, rgba(170,40,48,0.75), transparent 70%),
      radial-gradient(ellipse 220px 200px at 330px 540px, rgba(160,34,42,0.8), transparent 70%),
      radial-gradient(ellipse 200px 220px at 700px 520px, rgba(130,24,32,0.7), transparent 70%),
      radial-gradient(ellipse 160px 200px at 40px 200px, rgba(130,24,32,0.6), transparent 70%),
      radial-gradient(ellipse 260px 200px at 380px 960px, rgba(110,20,26,0.6), transparent 70%),
      linear-gradient(160deg, var(--cherry-mid), var(--cherry-deep) 70%);
  }

  .frame {
    position: absolute; left: 88px; top: 265px; width: 588px; height: 865px;
    border: 1.5px solid var(--frame);
  }

  .headline {
    position: absolute; left: 129px; top: 442px; width: 520px;
    font-family: "Montserrat", sans-serif; font-weight: 600; font-size: 20px;
    line-height: 27px; letter-spacing: 6px; color: var(--ink-light); text-transform: uppercase;
  }

  .fact-band {
    position: absolute; left: 0; top: 782px; width: 764px; height: 190px;
    background: var(--band);
  }
  .fact {
    position: absolute; right: 123px; top: 812px; width: 420px; text-align: right;
    font-family: "Roboto", sans-serif; font-weight: 300; font-size: 31px;
    line-height: 37px; color: var(--ink-light);
  }

  .benefits {
    position: absolute; left: 0; top: 992px; width: 764px; text-align: center;
    font-family: "Roboto", sans-serif; color: var(--ink-light);
  }
  .benefits-title { font-weight: 500; font-size: 24px; line-height: 32px; }
  .benefits-list { font-weight: 300; font-size: 18px; line-height: 23px; }
</style>
</head>
<body>
<main class="card">
  <header class="masthead">
    <span class="brand-dot"></span>
    <span class="brand-name">Ridgeline Orchards</span>
  </header>

  <div class="cherry-photo" role="img" aria-label="Close-up photograph of glossy dark red cherries with green stems and water droplets"></div>

  <div class="frame"></div>

  <h1 class="headline">Organic Ridgeline Cherries make up 1/3 of the nation’s production.</h1>

  <div class="fact-band"></div>
  <p class="fact">Washington State is the nation’s largest producer of organic cherries.</p>

  <section class="benefits">
    <h2 class="benefits-title">Health benefits:</h2>
    <p class="benefits-list">Fat Free | Source of Vitamin C | A Natural Anti-Inflammatory<br>Source of Potassium | Source of Melatonin</p>
  </section>
</main>
</body>
</html>
```